Supplement Package and Bottle Design*

We are a supplement company rebranding a number of product ranges for which we need a designer.

We will start with two products for joint health supplementation that are part of one range.

1. DERMINOX K48 Internal Oil Drops
The internal oil drop requires a design for the outer box and inside bottle label – see attached.

Front of box should include the following text:
- DERMINOX K48
- Internal Oil Drops
- Original formula from the oils of fresh Laurus nobilis L. leaves and Curcuma longa L. rhizomes
- Dilute before use
- Food supplement
- 100ml
- Some prominent icon/ graphics indicating use for joint health
- Selunetra logo

2. DERMINOX R5 External Cream
The external cream only requires a design for the bottle label – see attached.
- DERMINOX R5
- External Cream
- Original formula from the oils of fresh Laurus nobilis L. leaves + 7 select ingredients
- 150ml
- Selunetra logo

Overall design:
- Common design between both products (oil drops and cream)
Must appeal to a customer base of middle-age/ seniors
- Pharmaceutical product feel with touch of nature/ herbal remedy
- Design my convey a feeling of dependability, trust, effectiveness
- Premium product feel. These are very expensive products
- Design must be easy to adapt for new product ranges
- Use icons/ symbols to indicate health application, example: icon of knee to indicate use for joints
- "K48" and "R5" should be prominent to distinguish the products
- You have a choice of two Selunetra logos. See attached.
- Primary colours: white and rgb(33, 136, 135)
- Designers can also consider some use of stamped gold/ silver for embellishments

Once a successful design/ feel has been chosen then exact dielines will be provided.

Target Market(s)

Seniors (65+ years old) with arthritis. Generally retired and affluent.

Industry/Entity Type

Health Product

Colors
33b8a4

Requirements
Must have
• As per project description.

Please creatively use a laurel wreath in the design. Either as a standalone element or multiple laurel wreaths in the background of the design. Can be vector or blended image.

As the supplements are made from bay leaves (laurel leaves) this subtle connection should be present.
Should not have
• Should not be cheap design and loud.

Premium design that conveys trust and pharmaceutical grade treatment with embellishments reminding that this is a natural/ herbal remedy product

```html
<!DOCTYPE html>
<html lang="en">
<head>
<meta charset="utf-8">
<title>Derminox K48 and R5 Packaging</title>
<link href="https://fonts.googleapis.com/css2?family=Barlow+Condensed:wght@500;600;700&family=Barlow:wght@500&family=Open+Sans:wght@400&display=swap" rel="stylesheet">
<style>
:root{
  --teal:#1f8a87;
  --gold:#c9a227;
  --forest:#14302a;
  --leaf-a:#0f5a3c;
  --leaf-b:#2e8a5e;
  --ink:#2b2b2b;
  --rule:#9aa4a2;
  --white:#ffffff;
  --edge:#e4e8e7;
}
*{box-sizing:border-box;margin:0;padding:0}
html,body{width:1200px;height:821px;overflow:hidden;background:var(--white)}
.canvas{position:relative;width:1200px;height:821px;background:var(--white)}
.brand{font-family:"Barlow",sans-serif;font-weight:500;color:var(--gold);letter-spacing:.18em;text-align:center}
.product{font-family:"Barlow Condensed",sans-serif;font-weight:700;color:var(--teal);text-align:center;line-height:.9;letter-spacing:-.01em}
.code-row{display:flex;justify-content:center;align-items:center;gap:10px}
.code{font-family:"Barlow Condensed",sans-serif;font-weight:700;color:var(--gold);line-height:.9}
.wreath{display:block;flex:none}
.rule{height:1px;background:var(--rule)}
.type{font-family:"Barlow",sans-serif;font-weight:500;color:var(--teal);text-align:center;letter-spacing:.02em}
.copy{font-family:"Open Sans",sans-serif;color:var(--ink);text-align:center;line-height:1.35}
.leaves{background:linear-gradient(135deg,var(--leaf-a),var(--leaf-b) 45%,var(--leaf-a) 75%,#1f6e4a)}
.volume{font-family:"Barlow",sans-serif;font-weight:500;color:var(--white);text-align:center}
.panel{display:flex;flex-direction:column;background:var(--white);box-shadow:0 0 0 1px var(--edge)}
.panel .body{flex:1}

/* Box front */
.box-front{position:absolute;left:540px;top:80px;width:300px;height:560px}
.box-front .band-top{height:18px;background:var(--forest)}
.box-front .brand{margin-top:30px;font-size:22px}
.box-front .rule{margin:4px 30px 0}
.box-front .product{font-size:64px;margin-top:6px}
.box-front .code{font-size:58px}
.box-front .wreath{width:34px;height:54px}
.box-front .type{font-size:23px;margin-top:28px}
.box-front .supp{font-family:"Open Sans",sans-serif;font-size:16px;color:var(--ink);text-align:center;margin-top:2px}
.box-front .copy{font-size:13.5px;margin:16px 18px 0}
.box-front .band-mid{height:14px;background:var(--forest)}
.box-front .leaves{height:96px}
.box-front .band-bottom{height:72px;background:var(--forest);display:flex;align-items:center;justify-content:center}
.box-front .volume{font-size:24px}

/* Box side */
.box-side{position:absolute;left:840px;top:80px;width:82px;height:560px}
.box-side .band-top{height:18px;background:var(--forest)}
.box-side .brand{margin-top:32px;font-size:11px;letter-spacing:.08em}
.box-side .rule{margin:3px 6px 0}
.box-side .product{font-size:23px;margin-top:3px;letter-spacing:-.03em}
.box-side .code{font-size:24px}
.box-side .code-row{gap:3px}
.box-side .wreath{width:12px;height:26px}
.box-side .icons{display:flex;justify-content:space-around;margin-top:64px}
.box-side .icon{display:flex;flex-direction:column;align-items:center;gap:4px}
.box-side .joint{width:22px;height:80px}
.box-side .icon-label{font-family:"Barlow Condensed",sans-serif;font-weight:500;font-size:8px;color:var(--ink)}
.box-side .band-mid{height:14px;background:var(--forest)}
.box-side .leaves{height:96px}
.box-side .band-bottom{height:72px;background:var(--forest);display:flex;align-items:center;justify-content:center}
.box-side .dilute{font-family:"Barlow Condensed",sans-serif;font-weight:500;font-size:11px;color:var(--white);text-align:center}

/* Bottle label */
.bottle-label{position:absolute;left:940px;top:300px;width:180px;height:300px}
.bottle-label .band-top{height:12px;background:var(--forest)}
.bottle-label .brand{margin-top:14px;font-size:13px}
.bottle-label .rule{margin:3px 18px 0}
.bottle-label .product{font-size:38px;margin-top:4px}
.bottle-label .code{font-size:34px}
.bottle-label .wreath{width:22px;height:32px}
.bottle-label .type{font-size:13.5px;margin-top:16px}
.bottle-label .copy{font-size:9px;margin:16px 8px 0}
.bottle-label .leaves{height:40px}
.bottle-label .band-bottom{height:34px;background:var(--forest);display:flex;align-items:center;justify-content:center}
.bottle-label .volume{font-size:16px}

/* Cream label */
.cream-label{position:absolute;left:100px;top:520px;width:420px;height:150px;background:var(--white);box-shadow:0 0 0 1px var(--edge);display:flex}
.cream-label .band-top,.cream-label .band-bottom{position:absolute;left:0;right:0;height:10px;background:var(--forest)}
.cream-label .band-top{top:0}
.cream-label .band-bottom{bottom:0}
.cream-label .side{width:34px;background:var(--teal);margin:10px 0}
.cream-label .mark{width:150px;padding-top:18px}
.cream-label .brand{font-size:13px}
.cream-label .rule{margin:3px 10px 0}
.cream-label .product{font-size:36px;margin-top:2px}
.cream-label .code{font-size:36px}
.cream-label .wreath{width:20px;height:32px}
.cream-label .info{flex:1;position:relative;padding:10px 10px 0 6px}
.cream-label .leaves{height:44px}
.cream-label .type{text-align:left;font-family:"Barlow Condensed",sans-serif;font-weight:600;font-size:24px;margin-top:6px}
.cream-label .copy{font-size:9.5px;width:150px;margin-top:4px;margin-left:14px}
.cream-label .volume{position:absolute;right:10px;bottom:20px;font-family:"Barlow Condensed",sans-serif;font-weight:600;font-size:24px;color:var(--teal)}
</style>
</head>
<body>
<main class="canvas">

  <section class="cream-label" aria-label="Derminox R5 external cream label">
    <div class="band-top"></div>
    <div class="side"></div>
    <div class="mark">
      <p class="brand">SELUNETRA</p>
      <div class="rule"></div>
      <h2 class="product">DERMINOX</h2>
      <div class="rule"></div>
      <div class="code-row">
        <svg class="wreath" role="img" aria-label="Laurel branch" viewBox="0 0 20 32"><rect x="6" y="2" width="8" height="28" rx="4" fill="#1f8a87"/></svg>
        <span class="code">R5</span>
        <svg class="wreath" role="img" aria-label="Laurel branch" viewBox="0 0 20 32"><rect x="6" y="2" width="8" height="28" rx="4" fill="#1f8a87"/></svg>
      </div>
    </div>
    <div class="info">
      <div class="leaves" role="img" aria-label="Photo of fresh bay laurel leaves"></div>
      <p class="type">EXTERNAL CREAM</p>
      <p class="copy">Original formula from the oils of fresh Laurus nobilis L. leaves + 7 select ingredients</p>
      <p class="volume">150ml</p>
    </div>
    <div class="band-bottom"></div>
  </section>

  <section class="box-front panel" aria-label="Derminox K48 internal oil drops box front">
    <div class="band-top"></div>
    <div class="body">
      <p class="brand">SELUNETRA</p>
      <div class="rule"></div>
      <h1 class="product">DERMINOX</h1>
      <div class="rule"></div>
      <div class="code-row">
        <svg class="wreath" role="img" aria-label="Laurel wreath branch" viewBox="0 0 34 54"><rect x="11" y="4" width="12" height="46" rx="6" fill="#1f8a87"/></svg>
        <span class="code">K48</span>
        <svg class="wreath" role="img" aria-label="Laurel wreath branch" viewBox="0 0 34 54"><rect x="11" y="4" width="12" height="46" rx="6" fill="#1f8a87"/></svg>
      </div>
      <p class="type">INTERNAL OIL DROPS</p>
      <p class="supp">Food supplement</p>
      <p class="copy">Original formula from the oils of fresh Laurus nobilis L. leaves and Curcuma longa L. rhizomes</p>
    </div>
    <div class="band-mid"></div>
    <div class="leaves" role="img" aria-label="Photo of fresh bay laurel leaves"></div>
    <div class="band-bottom"><p class="volume">100ml</p></div>
  </section>

  <section class="box-side panel" aria-label="Derminox K48 box side panel">
    <div class="band-top"></div>
    <div class="body">
      <p class="brand">SELUNETRA</p>
      <div class="rule"></div>
      <p class="product">DERMINOX</p>
      <div class="rule"></div>
      <div class="code-row">
        <svg class="wreath" role="img" aria-label="Laurel wreath branch" viewBox="0 0 12 26"><rect x="3" y="2" width="6" height="22" rx="3" fill="#1f8a87"/></svg>
        <span class="code">K48</span>
        <svg class="wreath" role="img" aria-label="Laurel wreath branch" viewBox="0 0 12 26"><rect x="3" y="2" width="6" height="22" rx="3" fill="#1f8a87"/></svg>
      </div>
      <div class="icons">
        <div class="icon">
          <svg class="joint" role="img" aria-label="Knee joint icon" viewBox="0 0 22 80"><rect x="4" y="2" width="14" height="76" rx="3" fill="#4fb3ae"/></svg>
          <span class="icon-label">use for knees</span>
        </div>
        <div class="icon">
          <svg class="joint" role="img" aria-label="Hip joint icon" viewBox="0 0 22 80"><rect x="4" y="2" width="14" height="76" rx="3" fill="#4fb3ae"/></svg>
          <span class="icon-label">use for hips</span>
        </div>
      </div>
    </div>
    <div class="band-mid"></div>
    <div class="leaves" role="img" aria-label="Photo of fresh bay laurel leaves"></div>
    <div class="band-bottom"><p class="dilute">Dilute before use</p></div>
  </section>

  <section class="bottle-label panel" aria-label="Derminox K48 bottle label">
    <div class="band-top"></div>
    <div class="body">
      <p class="brand">SELUNETRA</p>
      <div class="rule"></div>
      <h2 class="product">DERMINOX</h2>
      <div class="rule"></div>
      <div class="code-row">
        <svg class="wreath" role="img" aria-label="Laurel wreath branch" viewBox="0 0 22 32"><rect x="7" y="2" width="8" height="28" rx="4" fill="#1f8a87"/></svg>
        <span class="code">K48</span>
        <svg class="wreath" role="img" aria-label="Laurel wreath branch" viewBox="0 0 22 32"><rect x="7" y="2" width="8" height="28" rx="4" fill="#1f8a87"/></svg>
      </div>
      <p class="type">INTERNAL OIL DROPS</p>
      <p class="copy">Original formula from the oils of fresh Laurus nobilis L. leaves and Curcuma longa L. rhizomes</p>
    </div>
    <div class="leaves" role="img" aria-label="Photo of fresh bay laurel leaves"></div>
    <div class="band-bottom"><p class="volume">100ml</p></div>
  </section>

</main>
</body>
</html>
```